New Business Card Design

We would like to refresh our business cards and make them look better. We are an IT company specialising in Cloud Services, IT Managed Services, software and hardware. I have attached a PSD of our current design. Also attached our logo.
Updates

I have uploaded all new logos in EPS format.

Can you please edit all designs to include a job title for Marcus Penn, eg. General Manager

Industry/Entity Type

Software

Colors
ffffff

Requirements
Must have
• Please use white background.
Should not have
• Black background

```html
<!DOCTYPE html>
<html lang="en">
<head>
<meta charset="utf-8">
<title>Business Card – Marcus Penn</title>
<link rel="stylesheet" href="https://fonts.googleapis.com/css2?family=Comfortaa:wght@400;700&family=Michroma&family=Share+Tech+Mono&display=swap">
<style>
  :root {
    --paper: #ffffff;
    --slate: #4b4f57;
    --slate-dark: #3f434a;
    --accent: #c8372a;
    --ink: #3a3d42;
    --backdrop: #e6e6e4;
  }
  * { margin: 0; padding: 0; box-sizing: border-box; }
  html, body { width: 1200px; height: 888px; overflow: hidden; }
  body {
    background: var(--backdrop);
    display: flex;
    align-items: center;
    justify-content: center;
    gap: 40px;
  }
  .card {
    width: 540px;
    height: 310px;
    position: relative;
    overflow: hidden;
    box-shadow: 0 4px 14px rgba(0,0,0,0.15);
  }

  /* front */
  .card--front { background: var(--paper); }
  .front__identity {
    position: absolute;
    left: 0; right: 0; top: 0;
    height: 168px;
    text-align: center;
    padding-top: 48px;
  }
  .front__name {
    font-family: "Michroma", sans-serif;
    font-weight: 400;
    font-size: 30px;
    letter-spacing: 2px;
    color: var(--ink);
  }
  .front__name-last { color: var(--accent); }
  .front__title {
    font-family: "Comfortaa", sans-serif;
    font-weight: 700;
    font-size: 17px;
    color: var(--ink);
    margin-top: 10px;
  }
  .front__web {
    font-family: "Share Tech Mono", monospace;
    font-size: 15px;
    color: var(--accent);
    margin-top: 24px;
    letter-spacing: 0.5px;
  }
  .front__band {
    position: absolute;
    left: 0; right: 0; bottom: 0;
    height: 128px;
    background: var(--slate);
    border-top: 5px solid var(--accent);
    padding: 26px 0 0 34px;
  }
  .front__contact {
    list-style: none;
    font-family: "Share Tech Mono", monospace;
    font-size: 16px;
    line-height: 24px;
    color: var(--paper);
    letter-spacing: 1px;
  }

  /* back */
  .card--back { background: var(--slate); }
  .back__brand {
    position: absolute;
    left: 0; right: 0; top: 0;
    height: 222px;
    display: flex;
    align-items: center;
    justify-content: center;
  }
  .back__name {
    font-family: "Comfortaa", sans-serif;
    font-weight: 700;
    font-size: 34px;
    letter-spacing: 1px;
    color: var(--paper);
  }
  .back__band {
    position: absolute;
    left: 0; right: 0; bottom: 0;
    height: 88px;
    background: var(--paper);
    border-top: 5px solid var(--accent);
    display: flex;
    align-items: center;
    justify-content: center;
  }
  .back__tagline {
    font-family: "Comfortaa", sans-serif;
    font-weight: 700;
    font-size: 14px;
    letter-spacing: 0.5px;
    color: var(--slate-dark);
  }
</style>
</head>
<body>
  <section class="card card--front" aria-label="Card front">
    <div class="front__identity">
      <h1 class="front__name">MARCUS <span class="front__name-last">PENN</span></h1>
      <p class="front__title">General Manager</p>
      <p class="front__web">www.claritynetit.com.au</p>
    </div>
    <div class="front__band">
      <ul class="front__contact">
        <li>P 07 3000 4141</li>
        <li>M 0400 512 377</li>
        <li>mpenn@claritynetit.com.au</li>
      </ul>
    </div>
  </section>

  <section class="card card--back" aria-label="Card back">
    <div class="back__brand">
      <span class="back__name">ClarityNet</span>
    </div>
    <div class="back__band">
      <p class="back__tagline">IT SERVICES, SOLUTIONS AND SUPPORT</p>
    </div>
  </section>
</body>
</html>
```